Rapidly growing regional logistics company looking for a modern clean website design.

We need a website for a 5 year old company based in New England.
We offer a complete logistics solution. With services dedicated to the changing economic environment. Services to our customers include, same day delivery, trucking and van service, warehouse & storage, pool distribution, and B2B installations.
We've implemented leading technology along the way, that provides visibility, accountability, up to the minute tracking, and project management.
Our goal to be known in the industry we service as an excellent provider of time-critical services and dependability.
Independently of the services we offer, our customers know that they can count on a true partner.

Target Market(s)

B2B, including printers, retail, manufacturers, wholesalers, electronics, any company that needs product delivered or warehoused

Industry/Entity Type

Logistics

Coding

Coded - Design and coding required

Number of Pages Required

5+ page

Font styles to use
Sans Serif

Colors
0255a3

Requirements
Must have
• Clean, modern design, limited clutter. Limited tabs, preferred everything on 1st screen roll down to see info

```html
<!DOCTYPE html>
<html lang="en">
<head>
<meta charset="utf-8">
<title>Halden Logistics</title>
<link href="https://fonts.googleapis.com/css2?family=Roboto+Condensed:wght@400;700&family=Open+Sans:wght@400;600&display=swap" rel="stylesheet">
<style>
:root{
  --blue:#0255a3;
  --ink:#1d1d1d;
  --text:#444;
  --muted:#666;
  --line:#d9d9d9;
  --panel:#efefef;
  --white:#fff;
  --icon-dark:#3a3a3a;
  --footer:#1c1f23;
  --head:"Roboto Condensed",Arial,sans-serif;
  --body:"Open Sans",Arial,sans-serif;
}
*{box-sizing:border-box;margin:0;padding:0}
html,body{width:1200px;height:3622px;overflow:hidden}
body{position:relative;background:var(--white);font-family:var(--body);color:var(--text)}
section,header,footer{position:absolute;left:0;width:1200px}
.abs{position:absolute}
.accent{color:var(--blue)}
h2{font-family:var(--head);font-weight:400;color:var(--ink);text-transform:none}

/* header */
.site-header{top:0;height:113px;border-top:4px solid var(--blue);background:var(--white)}
.brand{left:100px;top:14px;display:flex;align-items:center;gap:14px}
.brand-dot{width:80px;height:80px;border-radius:50%;background:var(--blue)}
.brand-name{font-family:var(--head);font-size:40px;font-weight:700;color:var(--blue);line-height:1;letter-spacing:1px}
.top-contact{right:100px;top:18px;display:flex;gap:34px;font-size:16px;color:var(--text);align-items:center}
.top-contact span{display:flex;align-items:center;gap:8px}
.main-nav{right:100px;top:70px;display:flex;gap:44px;font-family:var(--head);font-size:18px;color:#333}
.main-nav .active{color:var(--blue);font-weight:700}

/* hero */
.hero{top:113px;height:515px;background:linear-gradient(180deg,#c9a07a 0%,#e9c79d 32%,#b99778 55%,#5d5a5e 80%,#3b3d41 100%)}
.hero-arrow{top:240px;width:30px;height:30px;background:#222;display:flex;align-items:center;justify-content:center}
.hero-caption{left:0;bottom:0;width:1200px;height:53px;background:rgba(20,20,20,.72);color:var(--white);font-family:var(--head);font-size:29px;text-align:center;line-height:53px}

/* welcome */
.welcome{top:628px;height:550px}
.welcome h2{font-size:31px;text-transform:uppercase}
.rule{width:110px;height:2px;background:var(--ink);margin-top:6px}
.welcome-text{left:101px;top:50px;width:450px}
.welcome-text p{font-size:11.5px;line-height:22px;margin-top:12px;color:var(--text)}
.welcome-photo{left:109px;top:234px;width:434px;height:250px;background:linear-gradient(135deg,#8b6d4d,#d8c5a9 45%,#9fb4c8 70%,#6f5a44);box-shadow:0 0 0 6px #f2f2f2}
.modes{left:608px;top:50px;width:490px}
.mode{display:flex;gap:14px;margin-top:33px}
.mode:first-of-type{margin-top:40px}
.mode svg{flex:none;margin-top:2px}
.mode h3{font-family:var(--head);font-weight:400;font-size:16px;color:var(--ink);text-transform:uppercase}
.mode p{font-size:12.5px;line-height:19px;color:var(--muted);margin-top:4px}

/* services */
.services{top:1178px;height:464px;background:var(--panel)}
.section-title{width:1200px;text-align:center;font-size:32px}
.section-title::after{content:"";display:block;width:46px;height:2px;background:var(--blue);margin:10px auto 0}
.service-card{width:296px;height:128px;background:var(--white);display:flex;gap:18px;padding:22px 0 0 0}
.service-card .ico{width:80px;height:80px;flex:none;background:var(--icon-dark);display:flex;align-items:center;justify-content:center}
.service-card .ico.blue{background:var(--blue)}
.service-card h3{font-family:var(--head);font-weight:400;font-size:16.5px;color:var(--ink);margin-top:6px}
.service-card p{font-size:12px;line-height:18px;color:var(--muted);margin-top:6px}

/* supply chain */
.supply{top:1642px;height:439px}
.step{width:250px;text-align:center}
.step .ring{width:118px;height:118px;margin:0 auto;border-radius:50%;border:5px solid #d6d6d6;display:flex;align-items:center;justify-content:center}
.step .core{width:94px;height:94px;border-radius:50%;background:var(--icon-dark);display:flex;align-items:center;justify-content:center}
.step .core.blue{background:var(--blue)}
.step h3{font-family:var(--head);font-weight:400;font-size:18px;color:var(--ink);margin-top:22px}
.step p{font-size:12px;line-height:19px;color:var(--text);margin-top:6px}
.flow-arrow{top:204px}

/* technology */
.technology{top:2081px;height:389px;background:#f0f0f0}
.tablet{left:89px;top:75px;width:346px;height:222px;background:linear-gradient(135deg,#4b3a2e,#c7c7cb 30%,#f3f3f3 55%,#7d6a58);border-radius:8px;transform:skewX(-6deg)}
.tech-copy{left:459px;top:75px}
.tech-copy h2{font-size:29px;line-height:40px;color:var(--blue);width:640px}
.tech-copy ul{list-style:none;margin-top:8px;font-family:var(--head);font-size:20px;line-height:31px;color:var(--ink)}
.tech-copy li::before{content:"•";margin-right:10px}

/* reviews */
.reviews{top:2470px;height:504px;background:linear-gradient(180deg,#23303c 0%,#3c4651 45%,#27323d 75%,#1a2129 100%)}
.reviews .section-title{color:var(--white)}
.reviews .section-title::after{background:var(--white)}
.review{width:318px;text-align:center}
.avatar{width:82px;height:82px;border-radius:50%;margin:0 auto;background:linear-gradient(160deg,#d8cfc5,#9b8878);border:4px solid var(--white)}
.review h3{font-family:var(--head);font-weight:700;font-size:15px;color:var(--white);margin-top:16px}
.quote{margin-top:24px;height:102px;background:var(--white);text-align:left;padding:14px 18px 0 18px;font-size:12.5px;line-height:19px;color:var(--text);border-bottom:3px solid #bbb}
.quote b{font-family:Georgia,serif;font-size:26px;color:#aaa;vertical-align:-8px;margin-right:6px}
.rev-arrow{top:320px}

/* clients */
.clients{top:2974px;height:314px}
.client{top:147px;width:176px;height:97px;border:1px solid var(--line);display:flex;align-items:center;justify-content:center;font-family:var(--head);font-weight:700;font-size:22px;color:var(--ink)}
.client-arrow{top:184px}

/* footer */
.site-footer{top:3288px;height:334px;background:var(--footer);color:#cfcfcf}
.site-footer h4{font-family:var(--head);font-weight:400;font-size:19px;color:var(--white)}
.site-footer h4::after{content:"";display:block;width:150px;height:1px;background:#555;margin-top:8px}
.quick ul{list-style:none;margin-top:18px;font-size:12px;line-height:38px}
.quick li::before{content:"•";margin-right:10px;color:var(--white)}
.quick li.on{color:var(--white)}
.contact-list{margin-top:20px;font-size:12.5px;line-height:18px}
.contact-list div{display:flex;gap:12px;margin-bottom:22px}
.map{top:60px;width:266px;height:168px;background:linear-gradient(135deg,#dfe3d8,#f3efe6 50%,#cfd8e0)}
.social{display:flex;align-items:center;gap:12px;margin-top:22px}
.social .dot{width:30px;height:30px;border-radius:50%;background:#2d6fb5}
.social span{font-size:12px;color:var(--white);line-height:14px}
.social small{display:block;font-size:8px;color:#aaa}
.copyright{left:0;bottom:0;width:1200px;height:44px;background:var(--blue);color:var(--white);font-size:12px;text-align:center;line-height:44px}
</style>
</head>
<body>

<header class="site-header">
  <div class="brand abs">
    <div class="brand-dot"></div>
    <div class="brand-name">HALDEN<br><span style="font-weight:400;font-size:30px">LOGISTICS</span></div>
  </div>
  <div class="top-contact abs">
    <span><svg width="18" height="13" viewBox="0 0 18 13"><rect width="18" height="13" fill="#0255a3"/><path d="M0 0l9 7 9-7" stroke="#fff" fill="none"/></svg>inquiry@haldenlogistics.com</span>
    <span><svg width="18" height="18" viewBox="0 0 18 18"><circle cx="9" cy="9" r="9" fill="#0255a3"/><path d="M6 4l2 3-1 1c1 2 2 3 3 3l1-1 3 2-1 2c-4 0-8-4-8-8z" fill="#fff"/></svg>555.201.4860</span>
  </div>
  <nav class="main-nav abs">
    <span class="active">Home</span><span>About Us</span><span>Services</span><span>Careers</span><span>Contact Us</span>
  </nav>
</header>

<section class="hero" role="img" aria-label="Photo of a blue semi truck driving on a highway at sunset">
  <div class="hero-arrow abs" style="left:8px"><svg width="10" height="12"><path d="M8 1L2 6l6 5" stroke="#fff" stroke-width="2" fill="none"/></svg></div>
  <div class="hero-arrow abs" style="right:8px"><svg width="10" height="12"><path d="M2 1l6 5-6 5" stroke="#fff" stroke-width="2" fill="none"/></svg></div>
  <div class="hero-caption abs">Halden Logistics Offers A Complete Logistics Solutions.</div>
</section>

<section class="welcome">
  <div class="welcome-text abs">
    <h2>Welcome to <span class="accent">Halden Logistics</span></h2>
    <div class="rule"></div>
    <p>Our company was founded in 2012 but our team is seasoned, with a combined 75 years of experience. Halden Logistics offers a complete logistics solution. With services dedicated to the changing economic environment. Services to our customers include, same day delivery, trucking and van service.</p>
  </div>
  <div class="welcome-photo abs" role="img" aria-label="Photo of a smiling warehouse worker with a headset and clipboard"></div>
  <div class="modes abs">
    <h2>Lorem Ispum<span class="accent">Volumes</span></h2>
    <div class="rule"></div>
    <div class="mode">
      <svg width="46" height="26" viewBox="0 0 46 26"><rect x="0" y="2" width="28" height="16" fill="#0255a3"/><path d="M29 7h9l6 6v5H29z" fill="#0255a3"/><circle cx="9" cy="21" r="4" fill="#0255a3"/><circle cx="36" cy="21" r="4" fill="#0255a3"/></svg>
      <div><h3>Ground <span class="accent">Transport</span></h3><p>Lorem ipsum dolor sit amet, consectetuer adipiscing elit, sedammuny nibh euismod tincidunt ut laoreet dolore magna aliquam erat.</p></div>
    </div>
    <div class="mode">
      <svg width="46" height="26" viewBox="0 0 46 26"><path d="M2 13l40-4c3 0 3 8 0 8L2 13zM18 11l-6-10h5l12 10zM18 15l-6 10h5l12-10zM6 12l-4-6h3l6 6z" fill="#0255a3"/></svg>
      <div><h3>Air <span class="accent">Transport</span></h3><p>Lorem ipsum dolor sit amet, consectetuer adipiscing elit, sedammuny nibh euismod tincidunt ut laoreet dolore magna aliquam erat.</p></div>
    </div>
    <div class="mode">
      <svg width="46" height="26" viewBox="0 0 46 26"><rect x="10" y="2" width="20" height="10" fill="#0255a3"/><path d="M2 13h42l-6 10H7z" fill="#0255a3"/></svg>
      <div><h3>Ocean <span class="accent">Transport</span></h3><p>Lorem ipsum dolor sit amet, consectetuer adipiscing elit, sedammuny nibh euismod tincidunt ut laoreet dolore magna aliquam erat.</p></div>
    </div>
    <div class="mode">
      <svg width="46" height="26" viewBox="0 0 46 26"><rect x="6" y="8" width="18" height="12" fill="#0255a3"/><rect x="26" y="0" width="3" height="22" fill="#0255a3"/><rect x="29" y="18" width="12" height="3" fill="#0255a3"/><circle cx="10" cy="22" r="4" fill="#0255a3"/><circle cx="21" cy="22" r="4" fill="#0255a3"/></svg>
      <div><h3>Distributional <span class="accent">Transport</span></h3><p>Lorem ipsum dolor sit amet, consectetuer adipiscing elit, sedammuny nibh euismod tincidunt ut laoreet dolore magna aliquam erat.</p></div>
    </div>
  </div>
</section>

<section class="services">
  <h2 class="section-title abs" style="top:36px;text-transform:uppercase">Our <span class="accent">Services</span></h2>
  <div class="service-card abs" style="left:133px;top:118px">
    <div class="ico blue"><svg width="50" height="40" viewBox="0 0 50 40"><circle cx="16" cy="14" r="11" stroke="#fff" stroke-width="3" fill="none"/><path d="M16 8v7h5" stroke="#fff" stroke-width="2" fill="none"/><path d="M22 20h14l8 8v6H22z" fill="#fff"/><circle cx="28" cy="36" r="3" fill="#fff"/><circle cx="40" cy="36" r="3" fill="#fff"/></svg></div>
    <div><h3>Same Day <span class="accent">Delivery</span></h3><p>Donsectetuer adipiscing elit,<br>sedammuny nibh euismod tin</p></div>
  </div>
  <div class="service-card abs" style="left:456px;top:118px">
    <div class="ico"><svg width="50" height="34" viewBox="0 0 50 34"><rect x="2" y="4" width="30" height="20" fill="#fff"/><path d="M33 10h9l6 7v7H33z" fill="#fff"/><circle cx="12" cy="28" r="4" fill="#fff"/><circle cx="40" cy="28" r="4" fill="#fff"/></svg></div>
    <div><h3>Trucking &amp; Van <span class="accent">Service</span></h3><p>Donsectetuer adipiscing elit,<br>sedammuny nibh euismod tin</p></div>
  </div>
  <div class="service-card abs" style="left:780px;top:118px">
    <div class="ico"><svg width="46" height="40" viewBox="0 0 46 40"><path d="M2 14L23 2l21 12v24H2z" fill="#fff"/><rect x="11" y="18" width="24" height="20" fill="#3a3a3a"/><path d="M11 23h24M11 28h24M11 33h24" stroke="#fff" stroke-width="2"/></svg></div>
    <div><h3>Warehouse <span class="accent">&amp; Storage</span></h3><p>Donsectetuer adipiscing elit,<br>sedammuny nibh euismod tin</p></div>
  </div>
  <div class="service-card abs" style="left:133px;top:270px">
    <div class="ico"><svg width="46" height="40" viewBox="0 0 46 40"><rect x="4" y="14" width="18" height="16" fill="#fff"/><rect x="24" y="2" width="3" height="32" fill="#fff"/><rect x="27" y="30" width="14" height="3" fill="#fff"/><circle cx="9" cy="34" r="4" fill="#fff"/><circle cx="19" cy="34" r="4" fill="#fff"/></svg></div>
    <div><h3>Pool <span class="accent">Distribution</span></h3><p>Donsectetuer adipiscing elit,<br>sedammuny nibh euismod tin</p></div>
  </div>
  <div class="service-card abs" style="left:456px;top:270px">
    <div class="ico"><svg width="46" height="44" viewBox="0 0 46 44"><circle cx="20" cy="16" r="12" fill="#fff"/><path d="M8 42c0-10 24-10 24 0z" fill="#fff"/><circle cx="32" cy="10" r="8" fill="#3a3a3a" stroke="#fff" stroke-width="2"/><rect x="31" y="9" width="2" height="6" fill="#fff"/><rect x="31" y="5" width="2" height="2" fill="#fff"/></svg></div>
    <div><h3>Information <span class="accent">Services</span></h3><p>Donsectetuer adipiscing elit,<br>sedammuny nibh euismod tin</p></div>
  </div>
  <div class="service-card abs" style="left:780px;top:270px">
    <div class="ico"><svg width="50" height="34" viewBox="0 0 50 34"><path d="M2 8l10-6 8 4 6-2 8 4 14-4v16l-10 8-6 4-6-2-8-4-16-6z" fill="#fff"/><path d="M20 6l8 8 6-2" stroke="#3a3a3a" stroke-width="2" fill="none"/></svg></div>
    <div><h3>B2B <span class="accent">Installations</span></h3><p>Donsectetuer adipiscing elit,<br>sedammuny nibh euismod tin</p></div>
  </div>
</section>

<section class="supply">
  <h2 class="section-title abs" style="top:70px">Where We Fit <span class="accent">Into Your Supply Chain</span></h2>
  <div class="step abs" style="left:87px;top:166px">
    <div class="ring"><div class="core"><svg width="40" height="46" viewBox="0 0 40 46"><path d="M4 2h24l8 8v34H4z" fill="none" stroke="#fff" stroke-width="3"/><circle cx="14" cy="18" r="4" fill="#fff"/><circle cx="26" cy="30" r="4" fill="#fff"/><path d="M14 18l12 12" stroke="#fff" stroke-width="2"/></svg></div></div>
    <h3>Plan</h3><p>Lorem ipsum dolor sit amet&nbsp; sectetuer<br>adipiscing elit, sed diam.</p>
  </div>
  <div class="step abs" style="left:348px;top:166px">
    <div class="ring"><div class="core blue"><svg width="46" height="42" viewBox="0 0 46 42"><rect x="4" y="4" width="38" height="24" fill="none" stroke="#fff" stroke-width="3"/><circle cx="23" cy="16" r="5" fill="#fff"/><path d="M10 40c0-8 26-8 26 0z" fill="#fff"/></svg></div></div>
    <h3>Source / Make</h3><p>Lorem ipsum dolor sit amet&nbsp; sectetuer<br>adipiscing elit, sed diam.</p>
  </div>
  <div class="step abs" style="left:609px;top:166px">
    <div class="ring"><div class="core"><svg width="48" height="40" viewBox="0 0 48 40"><rect x="4" y="2" width="40" height="26" fill="none" stroke="#fff" stroke-width="3"/><rect x="12" y="10" width="14" height="10" fill="#fff"/><path d="M27 13h6l4 4v3H27z" fill="#fff"/><rect x="16" y="32" width="16" height="3" fill="#fff"/></svg></div></div>
    <h3>Book / Move</h3><p>Lorem ipsum dolor sit amet&nbsp; sectetuer<br>adipiscing elit, sed diam.</p>
  </div>
  <div class="step abs" style="left:870px;top:166px">
    <div class="ring"><div class="core blue"><svg width="46" height="46" viewBox="0 0 46 46"><circle cx="20" cy="12" r="8" fill="#fff"/><path d="M6 44c0-18 28-18 28 0z" fill="#fff"/><rect x="28" y="24" width="14" height="12" fill="#fff" stroke="#0255a3" stroke-width="2"/></svg></div></div>
    <h3>Deliver</h3><p>Lorem ipsum dolor sit amet&nbsp; sectetuer<br>adipiscing elit, sed diam.</p>
  </div>
  <svg class="flow-arrow abs" style="left:296px" width="96" height="24" viewBox="0 0 96 24"><defs><linearGradient id="ga" x1="0" x2="1"><stop offset="0" stop-color="#f2f2f2"/><stop offset="1" stop-color="#b5b5b5"/></linearGradient></defs><path d="M0 7h78V0l18 12-18 12v-7H0z" fill="url(#ga)"/></svg>
  <svg class="flow-arrow abs" style="left:557px" width="96" height="24" viewBox="0 0 96 24"><path d="M0 7h78V0l18 12-18 12v-7H0z" fill="url(#ga)"/></svg>
  <svg class="flow-arrow abs" style="left:818px" width="96" height="24" viewBox="0 0 96 24"><path d="M0 7h78V0l18 12-18 12v-7H0z" fill="url(#ga)"/></svg>
</section>

<section class="technology">
  <div class="tablet abs" role="img" aria-label="Tablet showing a tracking dashboard with charts"></div>
  <div class="tech-copy abs">
    <h2>We've implemented leading technology along the way,<br>that provides</h2>
    <ul><li>Visibility</li><li>Accountability</li><li>Upto the minute tracking</li><li>Project management</li></ul>
  </div>
</section>

<section class="reviews" role="img" aria-label="Dimmed photo of a harbour with cargo ships and cranes">
  <h2 class="section-title abs" style="top:48px">Happy Customer Reviews</h2>
  <svg class="rev-arrow abs" style="left:46px" width="20" height="44"><path d="M18 2L3 22l15 20" stroke="#ccc" stroke-width="2" fill="none"/></svg>
  <svg class="rev-arrow abs" style="right:46px" width="20" height="44"><path d="M2 2l15 20L2 42" stroke="#ccc" stroke-width="2" fill="none"/></svg>
  <div class="review abs" style="left:101px;top:161px">
    <div class="avatar" role="img" aria-label="Customer portrait"></div>
    <h3>Mr. Arlo Brenner</h3>
    <div class="quote"><b>“</b>Ut wisi enim ad minim veniam, quisilere mor nostrni exerci tation ullamcorperwer suskcipit no lobortis norl nislk ut aliquip.</div>
  </div>
  <div class="review abs" style="left:444px;top:161px">
    <div class="avatar" role="img" aria-label="Customer portrait"></div>
    <h3>Miss Nadia Vell</h3>
    <div class="quote"><b>“</b>Ut wisi enim ad minim veniam, quisilere mor nostrni exerci tation ullamcorperwer suskcipit no lobortis norl nislk ut aliquip.</div>
  </div>
  <div class="review abs" style="left:789px;top:161px">
    <div class="avatar" role="img" aria-label="Customer portrait"></div>
    <h3>Mr. Tomas Reuel</h3>
    <div class="quote"><b>“</b>Ut wisi enim ad minim veniam, quisilere mor nostrni exerci tation ullamcorperwer suskcipit no lobortis norl nislk ut aliquip.</div>
  </div>
</section>

<section class="clients">
  <h2 class="section-title abs" style="top:68px">Our <span class="accent">Clients</span></h2>
  <svg class="client-arrow abs" style="left:84px" width="14" height="24"><path d="M12 2L3 12l9 10" stroke="#333" stroke-width="3" fill="none"/></svg>
  <svg class="client-arrow abs" style="right:84px" width="14" height="24"><path d="M2 2l9 10-9 10" stroke="#333" stroke-width="3" fill="none"/></svg>
  <div class="client abs" style="left:121px">Norvale</div>
  <div class="client abs" style="left:316px">Brightwell</div>
  <div class="client abs" style="left:512px">Pantrico</div>
  <div class="client abs" style="left:707px">Fieldmark Foods</div>
  <div class="client abs" style="left:903px">Kestrel</div>
</section>

<footer class="site-footer">
  <div class="quick abs" style="left:100px;top:36px">
    <h4>Quick Link</h4>
    <ul><li class="on">Home</li><li>About Us</li><li>Services</li><li>Careers</li><li>Contact Us</li></ul>
  </div>
  <div class="abs" style="left:290px;top:36px">
    <h4>Contact Us</h4>
    <div class="contact-list">
      <div><svg width="12" height="16" viewBox="0 0 12 16"><path d="M6 0a6 6 0 016 6c0 4-6 10-6 10S0 10 0 6a6 6 0 016-6z" fill="#fff"/><circle cx="6" cy="6" r="2" fill="#1c1f23"/></svg><span>Halden Logistics<br>Street Name, City Name<br>State Zipcode</span></div>
      <div><svg width="14" height="14" viewBox="0 0 18 18"><path d="M4 1l4 5-2 2c1 2 3 4 5 5l2-2 5 4-2 3C8 18 0 10 1 3z" fill="#fff"/></svg><span style="font-size:15px">555.201.4860</span></div>
      <div><svg width="16" height="14" viewBox="0 0 16 14"><rect x="3" y="0" width="10" height="5" fill="#fff"/><rect x="0" y="5" width="16" height="7" fill="#fff"/><rect x="4" y="9" width="8" height="5" fill="#fff" stroke="#1c1f23"/></svg><span style="font-size:15px">555.201.4861</span></div>
      <div><svg width="16" height="12" viewBox="0 0 16 12"><rect width="16" height="12" fill="#fff"/><path d="M0 0l8 6 8-6" stroke="#1c1f23" fill="none"/></svg><span>inquiry@haldenlogistics.com</span></div>
    </div>
  </div>
  <div class="abs" style="left:609px;top:36px"><h4>Location Map</h4></div>
  <div class="map abs" style="left:609px;top:96px" role="img" aria-label="Street map showing the office location"></div>
  <div class="abs" style="left:945px;top:36px">
    <h4>Follow Us</h4>
    <div class="social"><div class="dot"></div><span>PAGEBOOK<small>BECOME A FAN</small></span></div>
    <div class="social"><div class="dot"></div><span>WORKLINE<small>JOIN US ON</small></span></div>
    <div class="social"><div class="dot"></div><span>CHIRPER<small>JOIN US ON</small></span></div>
  </div>
  <div class="copyright abs">Copyright © 2017 Halden Logistics. All Rights Reserved.</div>
</footer>

</body>
</html>
```